Stationary/business card for Custom Home builder
Pemberton Dwellings General Contractor
Simple
Travis Lindqvist
president
817 Calder Meadow Road
Dorrance Crossing, SC 29871
kbarlowbuilds@mailvero.net
Please use my logo

```html
<!DOCTYPE html>
<html lang="en">
<head>
<meta charset="utf-8">
<title>Pemberton Dwellings Stationery</title>
<link href="https://fonts.googleapis.com/css2?family=Cormorant+Garamond:wght@600&family=Open+Sans:wght@400;600&display=swap" rel="stylesheet">
<style>
  :root{
    --bg:#e9e6e2;
    --paper:#ffffff;
    --blue:#1f88d8;
    --blue-deep:#1466b0;
    --ink:#1b1b1b;
    --grey:#6d6d6d;
  }
  *{margin:0;padding:0;box-sizing:border-box}
  html,body{width:1200px;height:466px;overflow:hidden;background:var(--bg)}
  body{position:relative;font-family:"Open Sans",sans-serif;color:var(--ink)}
  .sheet{position:absolute;background:var(--paper);box-shadow:0 2px 6px rgba(0,0,0,.25);overflow:hidden}
  .swoosh{position:absolute;left:0;bottom:0;width:100%;display:block}
  .brand{font-family:"Cormorant Garamond",serif;font-weight:600;color:var(--blue-deep);line-height:1.05;text-transform:uppercase;letter-spacing:.04em;white-space:nowrap}
  .brand span{display:block}
  .brand small{display:block;font-size:.55em;letter-spacing:.08em;margin-top:1px}
  .contact{font-size:6px;line-height:1.55;color:var(--grey);white-space:nowrap}
  .contact b{font-weight:600;color:var(--ink)}

  /* business cards */
  .card-front{left:10px;top:163px;width:110px;height:70px}
  .card-front .brand{position:absolute;left:9px;top:12px;font-size:7px}
  .card-front .contact{position:absolute;right:8px;top:12px;font-size:4.5px;text-align:right}
  .card-back{left:10px;top:259px;width:110px;height:70px;background:var(--blue)}
  .card-back .brand{position:absolute;left:0;right:0;top:22px;text-align:center;font-size:10px;color:#fff}

  /* letterheads */
  .letterhead{top:43px;width:324px;height:413px}
  .letterhead.one{left:180px}
  .letterhead.two{left:528px}
  .letterhead .brand{position:absolute;left:26px;top:28px;font-size:13px}
  .letterhead .contact.top{position:absolute;left:196px;top:24px}
  .letterhead .contact.bottom{position:absolute;right:22px;bottom:92px;text-align:right}

  /* envelopes */
  .envelope{left:876px;width:300px}
  .env-a{top:48px;height:66px}
  .env-a .brand{position:absolute;right:14px;top:12px;font-size:10px}
  .env-b{top:124px;height:66px;background:var(--ink)}
  .env-b .stripe{position:absolute;left:0;right:0;top:30px;height:3px;background:var(--blue)}
  .env-c{top:200px;height:64px}
  .env-c .flap{position:absolute;inset:0;width:100%;height:100%}
  .env-c .brand{position:absolute;left:0;right:0;top:22px;text-align:center;font-size:11px}
  .env-front{top:288px;height:168px}
  .env-front .brand{position:absolute;left:16px;top:16px;font-size:13px}
  .env-front .contact{position:absolute;left:16px;top:52px}
</style>
</head>
<body>

<div class="sheet card-front">
  <div class="brand"><span>Pemberton</span><span>Dwellings</span></div>
  <div class="contact"><b>Travis Lindqvist</b><br>President<br>(843) 555-0192</div>
  <svg class="swoosh" viewBox="0 0 110 20" height="20" preserveAspectRatio="none" aria-hidden="true">
    <path d="M0 20 L0 10 Q55 22 110 2 L110 20Z" fill="var(--blue)"/>
    <path d="M0 8 Q55 20 110 0" stroke="var(--ink)" stroke-width="1.2" fill="none"/>
  </svg>
</div>

<div class="sheet card-back">
  <div class="brand"><span>Pemberton</span><span>Dwellings</span></div>
</div>

<div class="sheet letterhead one">
  <div class="brand"><span>Pemberton</span><span>Dwellings</span><small>General Contractor</small></div>
  <div class="contact top">
    <b>Travis Lindqvist</b><br>
    817 Calder Meadow Road<br>
    Dorrance Crossing, SC 29871<br>
    (843) 555-0192<br>
    kbarlowbuilds@mailvero.net
  </div>
  <svg class="swoosh" viewBox="0 0 324 90" height="90" preserveAspectRatio="none" aria-hidden="true">
    <defs><linearGradient id="lh1" x1="0" x2="1"><stop offset="0" stop-color="var(--blue-deep)"/><stop offset="1" stop-color="var(--blue)"/></linearGradient></defs>
    <path d="M0 90 L0 62 Q170 92 324 18 L324 90Z" fill="url(#lh1)"/>
    <path d="M0 56 Q170 86 324 10" stroke="var(--ink)" stroke-width="3" fill="none"/>
  </svg>
</div>

<div class="sheet letterhead two">
  <div class="contact bottom">
    <b>Travis Lindqvist</b><br>
    817 Calder Meadow Road<br>
    Dorrance Crossing, SC 29871<br>
    kbarlowbuilds@mailvero.net
  </div>
  <svg class="swoosh" viewBox="0 0 324 80" height="80" preserveAspectRatio="none" aria-hidden="true">
    <path d="M0 80 L0 20 Q150 80 324 60 L324 80Z" fill="var(--blue)"/>
    <path d="M0 14 Q150 74 324 54" stroke="var(--ink)" stroke-width="3" fill="none"/>
  </svg>
</div>

<div class="sheet envelope env-a">
  <div class="brand">Pemberton Dwellings</div>
  <svg class="swoosh" viewBox="0 0 300 30" height="30" preserveAspectRatio="none" aria-hidden="true">
    <path d="M0 30 L0 22 Q160 34 300 4 L300 30Z" fill="var(--blue)"/>
    <path d="M0 19 Q160 31 300 1" stroke="var(--ink)" stroke-width="1.5" fill="none"/>
  </svg>
</div>

<div class="sheet envelope env-b"><div class="stripe"></div></div>

<div class="sheet envelope env-c">
  <svg class="flap" viewBox="0 0 300 64" preserveAspectRatio="none" aria-hidden="true">
    <path d="M0 0 L150 40 L300 0" stroke="#d4d4d4" stroke-width="1" fill="none"/>
  </svg>
  <div class="brand">Pemberton Dwellings</div>
</div>

<div class="sheet envelope env-front">
  <div class="brand">Pemberton Dwellings<small>General Contractor</small></div>
  <div class="contact">817 Calder Meadow Road<br>Dorrance Crossing, SC 29871</div>
  <svg class="swoosh" viewBox="0 0 300 50" height="50" preserveAspectRatio="none" aria-hidden="true">
    <path d="M0 50 L0 8 Q120 46 300 40 L300 50Z" fill="var(--blue)"/>
    <path d="M0 3 Q120 41 300 35" stroke="var(--ink)" stroke-width="2" fill="none"/>
  </svg>
</div>

</body>
</html>
```